Modern Website Design for PollMeridian – CX & Loyalty SaaS Platform

We need a modern, professional, and responsive website design for our B2B SaaS platform, PollMeridian. We help companies collect real-time customer feedback, analyze insights, and improve loyalty — combining a powerful CX platform with expert consulting services. The website should clearly communicate who we are and what we offer within the first impression. It should balance data-driven visuals such as dashboards, analytics, and charts with a human, approachable feel. The design must include at least six key pages: Homepage, Product/Services, About, Blog/Resources, Contact/Demo, and Pricing. It should be conversion-focused with clear calls-to-action that encourage visitors to request a demo or contact us. The site must be fully responsive across desktop, tablet, and mobile. It should support multiple languages, starting with English and Danish. Most importantly, the delivery must be a final WordPress website, ready to go live, not just design files.

Target Market(s)

Our target market is medium-to-large B2B organizations. The primary audience includes CX leaders, executives, and managers in customer success and service who want to measure loyalty, understand customer insights, and improve retention.

Industry/Entity Type

Technology / SaaS / Customer Experience

Coding

Coded - Design and coding required

Number of Pages Required

5+ page

Font styles to use
Sans Serif

Requirements
Must have
• The project must deliver a final WordPress website that is fully responsive across all devices. The design should be clean, modern, and SaaS-inspired, with clear calls-to-action on every page. It must also support English and Danish, with a visible language toggle. The site should include visuals of dashboards and analytics that reflect data-driven insights. It must feature sections for case studies or testimonials to build trust. The copywriting should be SEO-friendly, and the design should include smooth animations or hover effects that add polish without making the website feel heavy.
Should not have
• Cluttered layouts, or generic stock photos such as handshakes

```html
<!DOCTYPE html>
<html lang="en">
<head>
<meta charset="utf-8">
<title>PollMeridian – CX & Loyalty Platform</title>
<link href="https://fonts.googleapis.com/css2?family=Inter:wght@400;500;600;700&display=swap" rel="stylesheet">
<style>
:root{
  --blue:#2463eb;
  --sky:#0ea5e9;
  --teal:#14b8a6;
  --ink:#1e293b;
  --muted:#64748b;
  --line:#e2e8f0;
  --hero-a:#eef6fd;
  --hero-b:#e3effd;
  --soft:#edf1f7;
  --footer:#1e293b;
  --canvas:#f1f4f8;
}
*{box-sizing:border-box;margin:0;padding:0}
html,body{width:1200px;height:1200px;overflow:hidden;background:var(--canvas);font-family:'Inter',sans-serif;color:var(--ink)}
.page{position:absolute;left:330px;top:0;width:852px;height:1890px;transform:scale(0.635);transform-origin:0 0;background:#fff;overflow:hidden}
section,header,footer{position:relative;overflow:hidden}
.abs{position:absolute}
.center{text-align:center;left:0;right:0}

/* nav */
.nav{height:38px;background:#fff;box-shadow:0 1px 4px rgba(15,23,42,.06);z-index:2}
.brand{left:94px;top:9px;display:flex;align-items:center;gap:6px;font-size:14px;font-weight:600;color:var(--blue)}
.brand i{width:12px;height:12px;background:var(--blue);border-radius:2px;display:block}
.menu{left:327px;top:12px;display:flex;gap:16px;font-size:8.5px;font-weight:500}
.nav-cta{left:616px;top:5px;width:90px;height:23px;border-radius:12px;background:var(--blue);color:#fff;font-size:8.5px;font-weight:600;display:flex;align-items:center;justify-content:center}
.lang{left:717px;top:12px;font-size:7.5px;color:var(--muted);display:flex;gap:5px;align-items:center}

/* hero */
.hero{height:515px;background:linear-gradient(160deg,var(--hero-a),var(--hero-b))}
.blob{position:absolute;border-radius:50%}
.hero h1{top:52px;font-size:30px;font-weight:700;line-height:36px;letter-spacing:-.3px}
.grad{background:linear-gradient(90deg,var(--blue),var(--teal));-webkit-background-clip:text;background-clip:text;color:transparent}
.hero .sub{top:140px;font-size:11.5px;line-height:17px;color:var(--muted)}
.btn{position:absolute;height:32px;border-radius:16px;font-size:8.5px;font-weight:600;display:flex;align-items:center;justify-content:center}
.btn-fill{left:324px;top:196px;width:106px;background:linear-gradient(90deg,var(--blue),var(--sky));color:#fff;box-shadow:0 4px 10px rgba(36,99,235,.3)}
.btn-line{left:441px;top:196px;width:85px;border:1px solid var(--blue);color:var(--blue);background:#fff}
.dash{left:177px;top:261px;width:497px;height:211px;background:#fff;border-radius:8px;box-shadow:0 10px 24px rgba(15,23,42,.12);padding:11px}
.dash-inner{width:100%;height:100%;border-radius:5px;background:linear-gradient(135deg,#e4eefc,#eaf0fb);display:flex;align-items:center;justify-content:center;gap:6px;font-size:9.5px;color:#7b8ba3}

/* features */
.why{height:523px;background:#fff}
.sec-title{font-size:22px;font-weight:600}
.sec-sub{font-size:10px;line-height:16px;color:var(--muted)}
.card{position:absolute;width:201px;background:#fff;border:1px solid #edf1f5;border-radius:8px;box-shadow:0 2px 8px rgba(15,23,42,.05);text-align:center;padding:22px 16px 0}
.icon{width:44px;height:44px;margin:0 auto;border-radius:9px;background:#e0edfd;display:flex;align-items:center;justify-content:center}
.card h3{margin-top:16px;font-size:13px;font-weight:600;line-height:21px}
.card p{margin-top:8px;font-size:8px;line-height:14px;color:var(--muted)}

/* testimonials */
.clients{height:350px;background:linear-gradient(180deg,#f1f4f9,var(--soft))}
.quote{position:absolute;top:175px;width:313px;height:152px;background:#fff;border-radius:8px;box-shadow:0 4px 14px rgba(15,23,42,.06);padding:22px 22px}
.quote p{font-size:9.5px;line-height:15.5px}
.who{display:flex;align-items:center;gap:8px;margin-top:14px}
.avatar{width:34px;height:34px;border-radius:50%;background:linear-gradient(135deg,var(--blue),var(--teal));display:flex;align-items:center;justify-content:center}
.who b{display:block;font-size:8.5px;font-weight:600}
.who span{font-size:7px;color:var(--muted)}

/* cta */
.cta{height:241px;background:linear-gradient(120deg,#2463eb,#0ea5e9);color:#fff}
.cta h2{top:58px;font-size:22px;font-weight:700}
.cta .sub{top:100px;font-size:10px;line-height:16px;color:#e0efff}
.btn-white{left:372px;top:154px;width:107px;border:1px solid #fff;color:#fff}

/* footer */
.footer{height:223px;background:var(--footer);color:#fff}
.col{position:absolute;top:45px;width:150px}
.col h4{font-size:11px;font-weight:600;margin-bottom:14px}
.col li{list-style:none;font-size:8px;color:#cbd5e1;margin-bottom:12px}
.col p{font-size:8px;line-height:14px;color:#cbd5e1}
.rule{left:105px;top:185px;width:642px;height:1px;background:#334155}
.copy{left:105px;top:203px;font-size:7px;color:#94a3b8}
.social{top:197px;width:20px;height:20px;border-radius:50%;background:#334155}
</style>
</head>
<body>
<div class="page">

  <header class="nav">
    <div class="abs brand"><i></i>PollMeridian</div>
    <nav class="abs menu"><span>Home</span><span>Platform</span><span>Services</span><span>About</span><span>Resources</span><span>Pricing</span></nav>
    <div class="abs nav-cta">Request Demo</div>
    <div class="abs lang"><span>EN</span><span>EN</span>
      <svg width="7" height="5" viewBox="0 0 7 5"><path d="M1 1l2.5 2.5L6 1" stroke="#475569" stroke-width="1.3" fill="none"/></svg>
    </div>
  </header>

  <section class="hero">
    <div class="blob" style="left:694px;top:-15px;width:216px;height:216px;background:#cfe3fb;opacity:.8"></div>
    <div class="blob" style="left:-62px;top:388px;width:200px;height:200px;background:#d4eef3;opacity:.9"></div>
    <h1 class="abs center">Measure, Understand, and<br><span class="grad">Improve Customer Loyalty</span></h1>
    <p class="abs center sub">Powerful CX platform combined with expert consulting to help<br>you reduce churn and drive growth.</p>
    <div class="btn btn-fill">Request a Demo</div>
    <div class="btn btn-line">Learn More</div>
    <div class="abs dash">
      <div class="dash-inner" role="img" aria-label="Interactive analytics dashboard preview">
        <svg width="12" height="11" viewBox="0 0 12 11"><path d="M1 0v10h11" stroke="#4a7ce0" stroke-width="1.4" fill="none"/><path d="M3.5 3h6M3.5 5.5h4M3.5 8h7" stroke="#4a7ce0" stroke-width="1.3"/></svg>
        Interactive Dashboard Preview
      </div>
    </div>
  </section>

  <section class="why">
    <h2 class="abs center sec-title" style="top:33px">Why Choose PollMeridian?</h2>
    <p class="abs center sec-sub" style="top:75px">We combine cutting-edge technology with human expertise to deliver<br>actionable insights.</p>

    <div class="card" style="left:106px;top:152px;height:172px">
      <div class="icon"><svg width="18" height="18" viewBox="0 0 18 18"><path d="M8 2a7 7 0 1 0 7 8H8z" fill="#2463eb"/><path d="M10 0v8h8A8 8 0 0 0 10 0z" fill="#2463eb"/></svg></div>
      <h3>Real-time Feedback</h3>
      <p>Collect and analyze customer feedback across multiple touchpoints in real-time.</p>
    </div>
    <div class="card" style="left:325px;top:152px;height:172px">
      <div class="icon"><svg width="22" height="16" viewBox="0 0 22 16"><circle cx="11" cy="4" r="3" fill="#2463eb"/><circle cx="4" cy="5" r="2.3" fill="#2463eb"/><circle cx="18" cy="5" r="2.3" fill="#2463eb"/><path d="M5 15a6 6 0 0 1 12 0z" fill="#2463eb"/><path d="M0 14a4 4 0 0 1 6-3.4L5 14zM22 14a4 4 0 0 0-6-3.4l1 3.4z" fill="#2463eb"/></svg></div>
      <h3>Expert Consulting</h3>
      <p>Our CX experts help you implement, interpret, and act on insights to drive results.</p>
    </div>
    <div class="card" style="left:543px;top:152px;height:172px">
      <div class="icon"><svg width="14" height="17" viewBox="0 0 14 17"><path d="M7 1a5 5 0 0 0-5 5v4L0 13h14l-2-3V6a5 5 0 0 0-5-5z" fill="#2463eb"/><circle cx="7" cy="15" r="2" fill="#2463eb"/></svg></div>
      <h3>Churn-risk Alerts</h3>
      <p>Get proactive notifications about at-risk customers so you can take action before it's too late.</p>
    </div>
    <div class="card" style="left:106px;top:341px;height:182px">
      <div class="icon"></div>
      <h3>Advanced Segmentation</h3>
      <p>Segment feedback by customer type, behavior, or demographics to uncover hidden insights.</p>
    </div>
    <div class="card" style="left:325px;top:341px;height:182px">
      <div class="icon"><svg width="13" height="17" viewBox="0 0 13 17"><path d="M0 1a1 1 0 0 1 1-1h7l5 5v11a1 1 0 0 1-1 1H1a1 1 0 0 1-1-1z" fill="#2463eb"/><path d="M3.5 9h6M3.5 11.5h6M3.5 14h6" stroke="#fff" stroke-width="1.1"/></svg></div>
      <h3>Leadership-ready<br>Reports</h3>
      <p>Automated reporting that provides executive-level insights at a glance.</p>
    </div>
    <div class="card" style="left:543px;top:341px;height:182px">
      <div class="icon"><svg width="15" height="17" viewBox="0 0 15 17"><path d="M7.5 0L15 3v5c0 4.5-3.3 8-7.5 9C3.3 16 0 12.5 0 8V3z" fill="#2463eb"/><path d="M7.5 3L12.5 5v3c0 3-2 5.5-5 6.5z" fill="#fff"/></svg></div>
      <h3>Enterprise Security</h3>
      <p>Bank-level security and compliance to keep your data safe and secure.</p>
    </div>
  </section>

  <section class="clients">
    <div class="blob" style="left:778px;top:-55px;width:110px;height:110px;background:#cfdff3"></div>
    <h2 class="abs center sec-title" style="top:58px">What Our Clients Say</h2>
    <p class="abs center sec-sub" style="top:100px">Hear from companies that have transformed their customer<br>experience with PollMeridian.</p>

    <div class="quote" style="left:105px">
      <p>"PollMeridian's platform combined with their expert consulting helped us reduce churn by 32% in the first quarter. Their insights were invaluable to our customer success strategy."</p>
      <div class="who"><div class="avatar"><svg width="12" height="12" viewBox="0 0 12 12"><circle cx="6" cy="3.5" r="2.8" fill="#fff"/><path d="M0.5 12a5.5 5 0 0 1 11 0z" fill="#fff"/></svg></div>
        <div><b>Lena Hartwell</b><span>CX Director, Brightline Corp.</span></div></div>
    </div>
    <div class="quote" style="left:434px">
      <p>"The real-time alerts have been a game-changer for our team. We can now address issues before they escalate, dramatically improving our customer retention."</p>
      <div class="who"><div class="avatar"><svg width="12" height="12" viewBox="0 0 12 12"><circle cx="6" cy="3.5" r="2.8" fill="#fff"/><path d="M0.5 12a5.5 5 0 0 1 11 0z" fill="#fff"/></svg></div>
        <div><b>Daniel Okafor</b><span>VP of Operations, Norvale Group</span></div></div>
    </div>
  </section>

  <section class="cta">
    <div class="blob" style="left:750px;top:-52px;width:160px;height:160px;background:#4ab0f2;opacity:.45"></div>
    <div class="blob" style="left:-60px;top:158px;width:132px;height:132px;background:#5b8cf0;opacity:.45"></div>
    <h2 class="abs center">Ready to Transform Your Customer Experience?</h2>
    <p class="abs center sub">Join hundreds of B2B companies using PollMeridian to boost loyalty<br>and drive growth.</p>
    <div class="btn btn-white">Request a Demo</div>
  </section>

  <footer class="footer">
    <div class="col" style="left:105px"><h4>PollMeridian</h4><p>Powerful CX platform combined with expert consulting services to help you measure and improve customer loyalty.</p></div>
    <div class="col" style="left:270px"><h4>Platform</h4><ul><li>Features</li><li>Integrations</li><li>Pricing</li><li>Security</li></ul></div>
    <div class="col" style="left:436px"><h4>Resources</h4><ul><li>Blog</li><li>Case Studies</li><li>Webinars</li><li>FAQ</li></ul></div>
    <div class="col" style="left:602px"><h4>Company</h4><ul><li>About Us</li><li>Careers</li><li>Contact</li><li>Privacy Policy</li></ul></div>
    <div class="abs rule"></div>
    <div class="abs copy">© 2023 PollMeridian. All rights reserved.</div>
    <div class="abs social" style="left:633px"></div>
    <div class="abs social" style="left:663px"></div>
    <div class="abs social" style="left:694px"></div>
    <div class="abs social" style="left:724px"></div>
  </footer>

</div>
</body>
</html>
```